Photographer website

This website will contain information to sell the services of marvello tebani an up and coming photographer based in london

Target Market(s)

SME's for corporate head shots
mums for kids parties
actors - for headshots
up and coming models

Industry/Entity Type

Photographer

Number of Pages Required

3 page

Requirements
Must have
• Home
• About me
• Contact me
• Portfolio or gallery

```html
<!DOCTYPE html>
<html lang="en">
<head>
<meta charset="utf-8">
<title>marvello tebani — Photography</title>
<link href="https://fonts.googleapis.com/css2?family=Raleway:wght@400;500&display=swap" rel="stylesheet">
<style>
  :root {
    --white: #ffffff;
    --ink: #3b3b3b;
    --active: #3b8fe0;
    --logo-box: #2a2a2a;
    --rule: #e4e4e4;
    --shadow-top: #9a9a9a;
    --shadow-bottom: #e9e9e9;
  }
  * { margin: 0; padding: 0; box-sizing: border-box; }
  html, body { width: 1200px; height: 3056px; overflow: hidden; background: var(--white); }
  body { font-family: 'Raleway', sans-serif; color: var(--ink); position: relative; }

  .hero {
    position: absolute; left: 0; top: 0; width: 1200px; height: 505px;
    background: radial-gradient(ellipse at 50% 45%, #4a6a74 0%, #234238 45%, #16302a 100%);
  }
  .hero-brand {
    position: absolute; left: 0; right: 0; top: 248px; text-align: center; color: var(--white);
  }
  .hero-brand .name { font-size: 30px; font-weight: 400; letter-spacing: 2px; }
  .hero-brand .enter { margin-top: 14px; font-size: 12px; letter-spacing: 2px; text-transform: uppercase; }

  .hero-shadow {
    position: absolute; left: 0; top: 505px; width: 1200px; height: 21px;
    background: linear-gradient(var(--shadow-top), var(--shadow-bottom));
  }

  .site-header {
    position: absolute; left: 0; top: 526px; width: 1200px; height: 73px; background: var(--white);
  }
  .logo-box {
    position: absolute; left: 90px; top: 0; width: 116px; height: 73px; background: var(--logo-box);
    color: var(--white); display: flex; align-items: center; justify-content: center;
    text-align: center; font-size: 14px; line-height: 1.2; letter-spacing: 1px;
  }
  .main-nav {
    position: absolute; right: 96px; top: 0; height: 73px; display: flex; align-items: center; gap: 24px;
    font-size: 13px;
  }
  .main-nav a { color: var(--ink); text-decoration: none; }
  .main-nav a.active { color: var(--active); }
  .social { display: flex; gap: 12px; margin-left: 4px; }
  .social span { width: 11px; height: 11px; border-radius: 50%; background: var(--ink); display: block; }

  .gallery {
    position: absolute; left: 0; top: 599px; width: 1200px; height: 2400px;
    display: grid; grid-template-columns: 400px 400px 400px; grid-template-rows: repeat(6, 400px);
  }
  .tile { position: relative; }
  .tile-meta {
    position: absolute; left: 22px; right: 22px; bottom: 18px; display: flex; justify-content: space-between;
    align-items: center; color: var(--white); font-size: 13px;
  }
  .likes { display: flex; align-items: center; gap: 8px; }

  .site-footer {
    position: absolute; left: 0; top: 2999px; width: 1200px; height: 57px;
    background: var(--white); border-top: 2px solid var(--rule);
  }
  .site-footer .social { position: absolute; right: 96px; top: 22px; }
</style>
</head>
<body>

<section class="hero" role="img" aria-label="Portrait photograph of a woman lying among dark green ivy leaves">
  <div class="hero-brand">
    <div class="name">marvello tebani</div>
    <div class="enter">Enter site</div>
  </div>
</section>
<div class="hero-shadow"></div>

<header class="site-header">
  <div class="logo-box">marvello<br>tebani</div>
  <nav class="main-nav">
    <a href="#">Welcome</a>
    <a href="#" class="active">Home</a>
    <a href="#">Gallery</a>
    <a href="#">About Me</a>
    <a href="#">Contact Me</a>
    <div class="social" aria-label="Social links"><span></span><span></span><span></span></div>
  </nav>
</header>

<main class="gallery">
  <div class="tile" style="background:linear-gradient(#e4e4e4,#c9c9c9)" role="img" aria-label="Black and white photo of a woman seated on a bench against a tiled wall">
    <div class="tile-meta">
      <span class="likes"><svg width="16" height="14" viewBox="0 0 16 14"><path d="M8 13 L2 7 A3.3 3.3 0 0 1 8 2.6 A3.3 3.3 0 0 1 14 7 Z" fill="none" stroke="#fff" stroke-width="1.4"/></svg>430</span>
      <svg width="14" height="14" viewBox="0 0 14 14"><path d="M6 2H2v10h10V8M8 2h4v4M12 2 6 8" fill="none" stroke="#fff" stroke-width="1.3"/></svg>
    </div>
  </div>
  <div class="tile" style="background:linear-gradient(#8a4a34,#4a3a30 50%,#2e2622)" role="img" aria-label="Photo of a person sitting on a wooden table by a brick wall"></div>
  <div class="tile" style="background:linear-gradient(135deg,#5a6a60,#7a5a48 60%,#c49a40)" role="img" aria-label="Portrait photo of a woman with teal hair and a shoulder tattoo"></div>

  <div class="tile" style="background:linear-gradient(#f0f0f0,#d6d6d6)" role="img" aria-label="Black and white photo of a smiling man in a cap and t-shirt"></div>
  <div class="tile" style="background:radial-gradient(ellipse at 50% 50%,#3c5a5a,#1a342c)" role="img" aria-label="Portrait photo of a woman lying among ivy leaves"></div>
  <div class="tile" style="background:linear-gradient(135deg,#6a6a6a,#5a5048 55%,#c8a030)" role="img" aria-label="Photo of a person in a black hat and yellow coat on a street">
    <div class="tile-meta">
      <span class="likes"><svg width="16" height="14" viewBox="0 0 16 14"><path d="M8 13 L2 7 A3.3 3.3 0 0 1 8 2.6 A3.3 3.3 0 0 1 14 7 Z" fill="none" stroke="#fff" stroke-width="1.4"/></svg>145</span>
      <svg width="14" height="14" viewBox="0 0 14 14"><path d="M6 2H2v10h10V8M8 2h4v4M12 2 6 8" fill="none" stroke="#fff" stroke-width="1.3"/></svg>
    </div>
  </div>

  <div class="tile" style="background:linear-gradient(#a8aca0,#6a6e64)" role="img" aria-label="Photo of a tattooed woman sitting on a sidewalk"></div>
  <div class="tile" style="background:radial-gradient(ellipse at 40% 50%,#5a5a5a,#222)" role="img" aria-label="Black and white photo of a woman casting a shadow on a wall"></div>
  <div class="tile" style="background:linear-gradient(#c4b49c,#a89c88 60%,#6a6a6a)" role="img" aria-label="Photo of a woman standing in a parking lot by a brick wall"></div>

  <div class="tile" style="background:linear-gradient(#b8b8b8,#8a8a8a)" role="img" aria-label="Photo of a man in glasses and a graphic t-shirt"></div>
  <div class="tile" style="background:linear-gradient(#8a8a88,#6c6c6a)" role="img" aria-label="Aerial photo of a man in a suit walking across asphalt"></div>
  <div class="tile" style="background:linear-gradient(#f0d038,#e4c02a 80%,#c8b070)" role="img" aria-label="Photo of a bicycle against a yellow corrugated wall"></div>

  <div class="tile" style="background:linear-gradient(#8a8a8a,#3e3e3e)" role="img" aria-label="Black and white photo of a woman's back with a spine tattoo">
    <div class="tile-meta">
      <span class="likes"><svg width="16" height="14" viewBox="0 0 16 14"><path d="M8 13 L2 7 A3.3 3.3 0 0 1 8 2.6 A3.3 3.3 0 0 1 14 7 Z" fill="none" stroke="#fff" stroke-width="1.4"/></svg>69</span>
      <svg width="14" height="14" viewBox="0 0 14 14"><path d="M6 2H2v10h10V8M8 2h4v4M12 2 6 8" fill="none" stroke="#fff" stroke-width="1.3"/></svg>
    </div>
  </div>
  <div class="tile" style="background:linear-gradient(#8a4e3a,#6e3e30 70%,#b88a7a)" role="img" aria-label="Photo of leopard print shoes on brick pavement"></div>
  <div class="tile" style="background:linear-gradient(#c0d0d2,#9ab4b8 55%,#5a7a80)" role="img" aria-label="Photo of a woman in a hoodie looking out over a lake"></div>

  <div class="tile" style="background:linear-gradient(#f2f2f2,#d8d8d8 70%,#9a9a9a)" role="img" aria-label="Photo of a skateboarder mid-trick"></div>
  <div class="tile" style="background:radial-gradient(ellipse at 50% 50%,#5a5a58,#232322)" role="img" aria-label="Photo of a bearded man in a hoodie and slogan t-shirt"></div>
  <div class="tile" style="background:linear-gradient(#dadada,#b8b8b8 55%,#9a7040)" role="img" aria-label="Photo of a person in a knit beanie and tan jacket seen from behind"></div>
</main>

<footer class="site-footer">
  <div class="social" aria-label="Social links"><span></span><span></span><span></span></div>
</footer>

</body>
</html>
```